Medical VIP club - small design

Please read the specs in a design brief attached. Also we don't have logo in a Vector format and attaching the only version we have.

Industry/Entity Type

Club

```html
<!DOCTYPE html>
<html lang="en">
<head>
<meta charset="utf-8">
<title>Vitacure — Medical VIP Club</title>
<link rel="stylesheet" href="https://fonts.googleapis.com/css2?family=PT+Sans:wght@400;700&family=EB+Garamond:wght@500&display=swap">
<style>
:root{
  --page:#5a4a38;
  --topbar:#3b2418;
  --gold:#8f6c1f;
  --gold-line:#8a6a22;
  --nav-text:#3b2610;
  --active-bg:#4a2b18;
  --active-text:#dcb262;
  --footer-link:#d9a834;
  --footer-muted:#8a6a2a;
  --logo-blue:#1a4f9c;
}
*{margin:0;padding:0;box-sizing:border-box}
html,body{width:1200px;height:745px;overflow:hidden}
body{background:var(--page);position:relative;font-family:"PT Sans",sans-serif}
.topbar{position:absolute;left:0;top:0;width:1200px;height:32px;background:var(--topbar)}
.frame{position:absolute;left:162px;top:32px;width:881px;height:671px;border:2px solid var(--gold-line);border-top:none;
  background:radial-gradient(ellipse 300px 90px at 50% 0,#7a6550,transparent 80%),var(--page)}
.logo-box{position:absolute;left:502px;top:10px;width:173px;height:89px;background:var(--topbar);padding:9px 7px}
.logo-inner{width:159px;height:72px;background:#fff;display:flex;align-items:center;justify-content:center;gap:6px}
.logo-inner .mark{width:14px;height:14px;border-radius:50%;background:var(--logo-blue)}
.logo-inner span{font-weight:700;font-size:26px;color:var(--logo-blue)}
.nav{position:absolute;left:164px;top:110px;width:877px;height:33px;background:var(--gold);display:flex;align-items:center}
.nav a{position:absolute;top:0;height:33px;line-height:35px;font-size:15px;color:var(--nav-text);text-decoration:none}
.nav a.active{background:var(--active-bg);color:var(--active-text);padding:0 11px}
.nav .dot{position:absolute;top:12px;width:10px;height:10px;border-radius:50%;background:#5e4a2c}
.hero{position:absolute;left:164px;top:143px;width:877px;height:324px}
.hero .side,.hero .main{position:absolute;top:0;height:324px}
.hero .side.left{left:0;width:172px;background:linear-gradient(180deg,#4a3a22,#6b5330 60%,#3a2e1c)}
.hero .main{left:172px;width:526px;background:radial-gradient(ellipse 120px 160px at 50% 40%,#d8b868,#8a6224 55%,#4a2e14)}
.hero .side.right{left:698px;width:179px;background:linear-gradient(180deg,#5a4a36,#7a6650 50%,#4a3a2a)}
.hero .arrow{position:absolute;top:128px;font-size:54px;color:#b89848;opacity:.8;font-family:"PT Sans",sans-serif}
.hero .caption{position:absolute;left:188px;top:248px;font-family:"EB Garamond",serif;font-size:23px;line-height:27px;color:#fff;letter-spacing:.6px;word-spacing:4px}
.member-strip{position:absolute;left:164px;top:467px;width:877px;height:20px;background:var(--gold)}
.member-strip .join{position:absolute;right:8px;top:0;line-height:21px;font-size:14px;color:var(--nav-text);display:flex;align-items:center;gap:7px}
.member-strip .dot{width:10px;height:10px;border-radius:50%;background:#5e4a2c;margin-right:8px}
.thumbs{position:absolute;top:487px;left:162px;height:126px}
.thumb{position:absolute;top:0;height:126px}
.gold-band{position:absolute;left:164px;top:613px;width:877px;height:22px;background:var(--gold)}
.footer{position:absolute;left:164px;top:635px;width:877px;height:66px}
.footer .flogo{position:absolute;left:14px;top:14px;display:flex;align-items:center;gap:6px;opacity:.55}
.footer .flogo .mark{width:12px;height:12px;border-radius:50%;background:#3b2a1c}
.footer .flogo span{font-weight:700;font-size:24px;color:#3b2a1c}
.footer-nav{position:absolute;left:264px;top:19px;font-family:Arial,sans-serif;font-size:12px;color:var(--footer-link)}
.footer-nav a{color:var(--footer-link);text-decoration:none;margin-right:9px}
.copyright{position:absolute;left:345px;top:42px;font-family:Arial,sans-serif;font-size:12px;color:var(--footer-link)}
.follow{position:absolute;right:16px;top:15px;font-family:Arial,sans-serif;font-size:12px;color:var(--footer-muted)}
.social{position:absolute;right:16px;top:35px;display:flex;gap:2px}
.social i{display:block;width:17px;height:17px;border-radius:2px}
</style>
</head>
<body>
<div class="topbar"></div>
<div class="frame"></div>

<div class="logo-box"><div class="logo-inner"><i class="mark"></i><span>vitacure</span></div></div>

<nav class="nav">
  <a style="left:39px">About Us</a><i class="dot" style="left:126px"></i>
  <a style="left:167px">VIP Club</a><i class="dot" style="left:248px"></i>
  <a style="left:286px">Services</a><i class="dot" style="left:367px"></i>
  <a style="left:406px">Packages and Prices</a><i class="dot" style="left:566px"></i>
  <a class="active" style="left:597px">Registration</a><i class="dot" style="left:721px"></i>
  <a style="left:760px">Contacts</a>
</nav>

<section class="hero">
  <div class="side left" role="img" aria-label="Photo of an ornate hotel entrance at dusk"></div>
  <div class="main" role="img" aria-label="Photo of a luxurious lit hotel corridor"></div>
  <div class="side right" role="img" aria-label="Photo of an elegant hallway with a staircase"></div>
  <span class="arrow" style="left:150px">‹</span>
  <span class="arrow" style="left:732px">›</span>
  <p class="caption">Lorem ipsum dolor sit amet,<br>consectetuer adipiscing elit.</p>
</section>

<div class="member-strip"><div class="join"><i class="dot"></i>Became a member
  <svg width="9" height="9" viewBox="0 0 9 9"><path d="M0 0L9 4.5 0 9z" fill="#e0b040"/></svg></div></div>

<div class="thumbs">
  <div class="thumb" style="left:0;width:178px;background:linear-gradient(135deg,#6a5640,#b8a88e 60%,#9a8a70)" role="img" aria-label="Photo of a hospital building with emergency signs"></div>
  <div class="thumb" style="left:179px;width:156px;background:linear-gradient(180deg,#3a3028,#8a7a66 55%,#2e241c)" role="img" aria-label="Photo of an airplane landing over a runway"></div>
  <div class="thumb" style="left:337px;width:189px;background:linear-gradient(135deg,#8a7a66,#d8d0c4 55%,#a89882)" role="img" aria-label="Photo of a team of doctors"></div>
  <div class="thumb" style="left:528px;width:166px;background:linear-gradient(180deg,#6aa0d8,#c8c0a8 45%,#3a9ab8)" role="img" aria-label="Photo of a villa terrace with a pool and palm trees"></div>
  <div class="thumb" style="left:696px;width:182px;background:linear-gradient(135deg,#7a6a58,#a8988a 60%,#8a7a68)" role="img" aria-label="Photo of a hospital direction sign"></div>
</div>

<div class="gold-band"></div>

<footer class="footer">
  <div class="flogo"><i class="mark"></i><span>vitacure</span></div>
  <nav class="footer-nav"><a>About Us</a><a>VIP Club</a> <a>Services</a><a>Packages and Prices</a> <a>Registration</a> <a>Contacts</a></nav>
  <p class="copyright">© Copyright Vitacure Ltd. All Rights Reserved</p>
  <p class="follow">Follow Us</p>
  <div class="social" aria-label="Social links">
    <i style="background:#5cc4e8"></i><i style="background:#e88a2a"></i><i style="background:#3b5a9a"></i>
  </div>
</footer>
</body>
</html>
```